Email Marketing Campaign Templates

Email drip childcare campaign designed to communicate with parents interested in services. We would like the template(s) to be created so that we can change the content as needed.I will add below collateral that we have used in the past as well as logo.
three to for templates 1.) welcome template 2/ things to bring 3) generic template
Target Market(s)
Parents and Millennials
Industry/Entity Type
Childcare
Colors
85cae6
0493ce
9bcb3c
add136
fefefe
faa54b
cadf82
86cae7
33a6d7
Requirements
Must have
- Photos of staff with children
Nice to have
- Photos

```html
<!DOCTYPE html>
<html lang="en">
<head>
<meta charset="utf-8">
<title>Bloomwell Early Learning – Email Templates</title>
<link rel="stylesheet" href="https://fonts.googleapis.com/css2?family=Patrick+Hand+SC&family=Varela+Round&display=swap">
<style>
  :root {
    --sky: #85cae6;
    --ocean: #0493ce;
    --leaf: #9bcb3c;
    --lime: #cadf82;
    --sun: #fbe26a;
    --tangerine: #faa54b;
    --paper: #fefefe;
    --frame: #4a78b8;
    --heading-font: "Patrick Hand SC", cursive;
    --body-font: "Varela Round", sans-serif;
  }
  * { box-sizing: border-box; margin: 0; padding: 0; }
  html, body { width: 849px; height: 1200px; overflow: hidden; background: var(--paper); }
  .canvas { position: relative; width: 849px; height: 1200px; }

  .email { position: absolute; left: 62px; width: 707px; height: 350px; border: 1px solid var(--frame); background: var(--paper); overflow: hidden; }
  .email--welcome { top: 27px; }
  .email--bring { top: 407px; }
  .email--generic { top: 789px; }

  .sidebar { position: absolute; left: 0; top: 0; width: 225px; height: 100%; }
  .brand { position: absolute; left: 48px; top: 58px; display: flex; align-items: center; gap: 8px; }
  .brand__dot { width: 22px; height: 22px; border-radius: 50%; background: var(--leaf); }
  .brand__name { font-family: var(--body-font); font-size: 21px; color: var(--ocean); }

  .sidebar__title { position: absolute; left: 20px; width: 190px; text-align: center; font-family: var(--heading-font); color: var(--leaf); font-size: 38px; line-height: 30px; }
  .sidebar__text { position: absolute; left: 21px; width: 185px; font-family: var(--body-font); font-size: 13.5px; line-height: 19.5px; color: var(--ocean); }

  .strip { position: absolute; left: 224px; top: 0; width: 73px; height: 100%; }
  .strip--blue { background: linear-gradient(180deg, #1a9bd7, var(--ocean)); }
  .strip--green { background: linear-gradient(180deg, #9fd13f, var(--leaf)); }

  .tile { position: absolute; display: flex; align-items: center; justify-content: center; text-align: center; font-family: var(--heading-font); color: var(--paper); font-size: 44px; line-height: 38px; }
  .tile--orange { background: var(--tangerine); }
  .tile--blue { background: var(--sky); }
  .tile--green { background: var(--lime); }
  .photo { position: absolute; }

  .generic__header { position: absolute; left: 297px; top: 0; width: 410px; height: 79px; background: var(--tangerine); font-family: var(--heading-font); color: var(--paper); font-size: 40px; line-height: 79px; padding-left: 24px; letter-spacing: 1px; }
  .generic__body { position: absolute; left: 297px; top: 79px; width: 410px; height: 271px; background: var(--ocean); padding: 17px 20px 0 24px; font-family: var(--body-font); font-size: 14px; line-height: 19.6px; color: var(--paper); }
</style>
</head>
<body>
<main class="canvas">

  <section class="email email--welcome">
    <div class="sidebar">
      <div class="brand"><span class="brand__dot"></span><span class="brand__name">Bloomwell</span></div>
      <h2 class="sidebar__title" style="top:186px">WELCOME</h2>
      <p class="sidebar__text" style="top:234px">At Bloomwell each child's needs and interests are built on in a caring and loving.</p>
    </div>
    <div class="strip strip--blue" role="img" aria-label="Pattern of white hand-drawn toys, rainbows, rockets and boats"></div>
    <div class="tile tile--orange" style="left:297px;top:0;width:211px;height:116px">NURTURE</div>
    <div class="photo" role="img" aria-label="Teacher reading a book with young children" style="left:508px;top:0;width:199px;height:116px;background:linear-gradient(135deg,#e9e4df,#c9a992)"></div>
    <div class="photo" role="img" aria-label="Child painting at a table" style="left:297px;top:116px;width:211px;height:133px;background:linear-gradient(135deg,#f9e15a,#f2c93c)"></div>
    <div class="tile tile--blue" style="left:508px;top:116px;width:199px;height:133px">FLOURISH</div>
    <div class="tile tile--green" style="left:297px;top:249px;width:211px;height:101px">GROW</div>
    <div class="photo" role="img" aria-label="Toddlers playing with building blocks" style="left:508px;top:249px;width:199px;height:101px;background:linear-gradient(135deg,#efe7e0,#d7b8a4)"></div>
  </section>

  <section class="email email--bring">
    <div class="sidebar">
      <div class="brand"><span class="brand__dot"></span><span class="brand__name">Bloomwell</span></div>
      <h2 class="sidebar__title" style="top:186px">WHAT TO<br>BRING</h2>
      <p class="sidebar__text" style="top:250px">At Bloomwell each child's needs and interests are built on in a caring. And loving environment.</p>
    </div>
    <div class="strip strip--blue" role="img" aria-label="Pattern of white hand-drawn toys, moons, bears and pencils"></div>
    <div class="tile tile--green" style="left:297px;top:0;width:187px;height:120px">LUNCH</div>
    <div class="photo" role="img" aria-label="Lunch box with a playful sandwich and fruit" style="left:484px;top:0;width:223px;height:120px;background:linear-gradient(135deg,#f2efe9,#d9b27a)"></div>
    <div class="photo" role="img" aria-label="Pencils and craft paper on a desk" style="left:297px;top:120px;width:187px;height:111px;background:linear-gradient(135deg,#f3ece3,#d6b48a)"></div>
    <div class="tile tile--blue" style="left:484px;top:120px;width:223px;height:111px">PEN &amp;<br>PAPER</div>
    <div class="tile tile--orange" style="left:297px;top:231px;width:187px;height:119px">EXTRA<br>CLOTHING</div>
    <div class="photo" role="img" aria-label="Folded children's clothes topped with small shoes" style="left:484px;top:231px;width:223px;height:119px;background:linear-gradient(180deg,#f8e06a,#e8d4e6)"></div>
  </section>

  <section class="email email--generic">
    <div class="sidebar">
      <div class="brand"><span class="brand__dot"></span><span class="brand__name">Bloomwell</span></div>
    </div>
    <div class="strip strip--green" role="img" aria-label="Pattern of white hand-drawn toys, rockets, crabs and boats"></div>
    <h2 class="generic__header">GENERIC TEMPLATE</h2>
    <p class="generic__body">At Bloomwell each child's needs and interests are built on in a caring and loving environment. We have a deep appreciation of the significance of developing each child's potential, at their own pace, and our devoted team aim to provide a warm and welcoming environment, full of stimulating experiences and<br>discoveries.</p>
  </section>

</main>
</body>
</html>
```